Online Certificate in Research Methods needs a Digital Banner ad

We are launching an online graduate certificate in Quantitative and Qualitative Social Science Research Methods. We need a digital banner created so we can advertise on pagenook, seekora, and some other places.

The banner needs to use these color schemes and fonts: https://universityrelations.bmlu.edu/brand-guide/color

Would like the banner to say (either as three lines, or if not in three lines, have these sets of words at minimum on the same line):
Online Graduate Certificate in
Quantitative & Qualitative
Social Science Research Methods

We also want it to say Brennmoor Lake University and Next Start Date August 18, 2021. I’ve attached a picture of a version we tried to create but is hard to read.

We need a graphic that looks good in the following specs:
600px wide x 70px tall, high quality (at least 300 dpi) jpg or png

And
Pagenook recommendations:
Design Recommendations
• File Type: JPG or PNG
• Ratio: 1.91:1 to 1:1
• Resolution: At least 1080 x 1080 pixels
Text Recommendations
• Primary Text: 125 characters
• Headline: 40 characters
• Description: 30 characters
Technical Requirements
• Maximum File Size: 30MB
• Minimum Width: 600 pixels
• Minimum Height: 600 pixels
• Aspect Ratio Tolerance: 3%

```html
<!DOCTYPE html>
<html lang="en">
<head>
<meta charset="utf-8">
<title>Brennmoor Lake University – Online Graduate Certificate Banner</title>
<link rel="stylesheet" href="https://fonts.googleapis.com/css2?family=Arimo:wght@700&display=swap">
<style>
  :root {
    --gold: #EAAA00;
    --navy: #002855;
    --white: #FFFFFF;
    --photo-dark: #3b3a42;
    --photo-mid: #5f7698;
    --photo-blue: #4a78b4;
    --photo-light: #a9bccf;
  }
  * { margin: 0; padding: 0; box-sizing: border-box; }
  html, body {
    width: 1200px;
    height: 1200px;
    overflow: hidden;
    background: var(--white);
  }
  .banner {
    position: relative;
    width: 1200px;
    height: 1200px;
    overflow: hidden;
    font-family: "Arimo", Arial, sans-serif;
    font-weight: 700;
  }
  .banner__photo {
    position: absolute;
    left: 0;
    top: 244px;
    width: 1200px;
    height: 956px;
    background:
      radial-gradient(ellipse 420px 520px at 230px 620px, rgba(70,55,50,0.55), transparent 70%),
      radial-gradient(ellipse 380px 300px at 1000px 900px, rgba(235,238,242,0.7), transparent 70%),
      linear-gradient(100deg, var(--photo-dark) 0%, var(--photo-mid) 35%, var(--photo-blue) 62%, var(--photo-light) 100%);
  }
  .banner__shapes {
    position: absolute;
    left: 0;
    top: 0;
    width: 1200px;
    height: 1200px;
  }
  .brand {
    position: absolute;
    left: 44px;
    top: 70px;
    display: flex;
    align-items: center;
    gap: 22px;
    color: var(--navy);
  }
  .brand__mark {
    width: 84px;
    height: 84px;
    background: var(--navy);
  }
  .brand__name {
    font-size: 52px;
    letter-spacing: -0.5px;
    line-height: 1;
  }
  .headline {
    position: absolute;
    right: 50px;
    top: 378px;
    text-align: right;
    color: var(--white);
    font-size: 54px;
    line-height: 64px;
    font-variant: small-caps;
    letter-spacing: 1px;
  }
  .start-date {
    position: absolute;
    left: 448px;
    width: 500px;
    top: 642px;
    text-align: center;
    color: var(--white);
    font-size: 54px;
    line-height: 62px;
    font-variant: small-caps;
    letter-spacing: 1px;
  }
</style>
</head>
<body>
  <main class="banner">
    <div class="banner__photo" role="img" aria-label="Photo of a student writing notes at a table beside a tablet on a stand"></div>

    <svg class="banner__shapes" viewBox="0 0 1080 1080" aria-hidden="true">
      <rect class="top-band" x="0" y="0" width="1080" height="208" fill="var(--gold)"/>
      <rect class="top-rule" x="0" y="208" width="1080" height="12" fill="var(--navy)"/>
      <polygon class="navy-stripe" points="943,0 1077,0 860,325 722,325" fill="var(--navy)"/>
      <polygon class="gold-stripe" points="483,722 625,722 395,1080 255,1080" fill="var(--gold)"/>
    </svg>

    <div class="brand">
      <span class="brand__mark"></span>
      <span class="brand__name">Brennmoor Lake University</span>
    </div>

    <h1 class="headline">
      Online Graduate Certificate in<br>
      Quantitative &amp; Qualitative<br>
      Social Science Research Methods
    </h1>

    <p class="start-date">
      Next Start Date<br>
      August 18, 2021
    </p>
  </main>
</body>
</html>
```